Corvale Holdings Business Cards

Hello. I need business cards designed with our new logo. I'd like to see at least 3 different designs. At least one with a dark background, and at least one with a white background. Maybe one with gray or blue for the background. Play with gradient colors and maybe even insert a pic of a skyline in the background of one or more of them. Use your judgement. We will need 2 cards printed. They need to accommodate the employee name, title, company address, phone, email, and website. Thanks.

Target Market(s)

Wealthy mature investors.

Contact Information for Business Card

Single-sided, professional, clean design that incorporates our logo.

Font styles to use
Sans Serif

Requirements
Must have
• Our new logo needs to be featured on it. (See attached.)
• Employee Name (In all CAPS)
• Title
• Street Address, City, ST Zip Code
• Cell Phone #, Email Address, Website Address
Nice to have
• Design that blends well with our new logo and its colors, or a city scape or other graphic design that looks like an apartment complex in the background. Blues and grays are nice, but use your judgement.
Should not have
• Modern or oriental looking designs or bright colors.

```html
<!DOCTYPE html>
<html lang="en">
<head>
<meta charset="utf-8">
<title>Corvale Holdings Business Cards</title>
<link href="https://fonts.googleapis.com/css2?family=Montserrat:wght@400;500&display=swap" rel="stylesheet">
<style>
  :root {
    --backdrop: #3a3531;
    --card: #232323;
    --card-edge: #1a1a1a;
    --blue: #2aa8e2;
    --gray: #6e6e6e;
    --gray-light: #8a8a8a;
  }
  * { box-sizing: border-box; margin: 0; padding: 0; }
  html, body {
    width: 1200px; height: 672px; overflow: hidden;
    background: var(--backdrop);
    font-family: "Montserrat", sans-serif;
  }
  .stage { position: relative; width: 1200px; height: 672px; }
  .card {
    position: absolute; top: 56px;
    width: 320px; height: 560px;
    background: var(--card);
    border: 1px solid var(--card-edge);
    box-shadow: 0 10px 30px rgba(0,0,0,.45);
    overflow: hidden;
  }
  .card--front { left: 250px; }
  .card--back { left: 630px; }

  /* front content is laid out landscape then turned to read top-to-bottom */
  .front-layout {
    position: absolute; top: 0; left: 0;
    width: 560px; height: 320px;
    transform-origin: 0 0;
    transform: translate(320px, 0) rotate(90deg);
  }
  .brand {
    position: absolute; left: 34px; top: 58px;
  }
  .brand__name {
    color: var(--blue); font-weight: 500;
    font-size: 30px; letter-spacing: 1px; line-height: 1;
  }
  .brand__sub {
    color: var(--gray); font-weight: 500;
    font-size: 14px; letter-spacing: 1.5px; margin-top: 6px;
  }
  .divider {
    position: absolute; left: 290px; top: 22px;
    width: 1.5px; height: 150px; background: var(--blue);
  }
  .contact {
    position: absolute; left: 312px; top: 26px;
    color: var(--gray); font-size: 12px; line-height: 1.9;
  }
  .contact__name {
    font-size: 19px; letter-spacing: 1px; color: var(--gray-light); line-height: 1.2;
  }
  .contact__license { color: var(--blue); font-size: 12px; margin-bottom: 4px; }
  .contact__row { display: flex; align-items: center; gap: 7px; }
  .contact__row svg { width: 10px; height: 10px; fill: none; stroke: var(--gray); stroke-width: 1.5; }
  .contact__address { margin-top: 2px; }

  .back-brand {
    position: absolute; left: 30px; bottom: 40px;
    display: flex; align-items: center; gap: 12px;
  }
  .back-brand__mark { width: 26px; height: 26px; background: var(--gray); }
  .back-brand__name {
    color: var(--blue); font-weight: 500;
    font-size: 19px; letter-spacing: 1px; line-height: 1.15;
  }
</style>
</head>
<body>
<main class="stage">
  <section class="card card--front">
    <div class="front-layout">
      <div class="brand">
        <div class="brand__name">CORVALE</div>
        <div class="brand__sub">HOLDINGS, LLC</div>
      </div>
      <div class="divider"></div>
      <div class="contact">
        <div class="contact__name">YOUR NAME</div>
        <div class="contact__license">CA LIC/ #604215</div>
        <div class="contact__row">
          <svg viewBox="0 0 10 10"><path d="M2 1h2l1 2-1.2 1a5 5 0 0 0 2.2 2.2L7 5l2 1v2a1 1 0 0 1-1 1A7 7 0 0 1 1 2a1 1 0 0 1 1-1z"/></svg>
          <span>000 000 0000</span>
        </div>
        <div class="contact__row">
          <svg viewBox="0 0 10 10"><rect x="1" y="2" width="8" height="6"/><path d="M1 2l4 3.5L9 2"/></svg>
          <span>youremail@xyz.com</span>
        </div>
        <div class="contact__row">
          <svg viewBox="0 0 10 10"><circle cx="5" cy="5" r="4"/><path d="M1 5h8M5 1c2 2.5 2 5.5 0 8M5 1c-2 2.5-2 5.5 0 8"/></svg>
          <span>www.yourwebsite.com</span>
        </div>
        <div class="contact__address">Street Address, City, ST Zip Code</div>
      </div>
    </div>
  </section>

  <section class="card card--back">
    <div class="back-brand">
      <div class="back-brand__mark"></div>
      <div class="back-brand__name">CORVALE<br>HOLDINGS, LLC</div>
    </div>
  </section>
</main>
</body>
</html>
```